Lumer product box design professional skincare

Design a professional skincare box that looks clean and modern. Based on the label. We need a professional look. It needs to be outstanding from other brands on the market. It is going to be a luxury market product. The box should fit multiple products, so the box should stay multifunctional, yet very professional.

Target Market(s)

skincare, beauty

Industry/Entity Type

Skin Care Product

Requirements
Must have
• Include logo
• Include: Professional Skincare Therapies

```html
<!DOCTYPE html>
<html lang="en">
<head>
<meta charset="utf-8">
<title>Lumer — Skincare Box Panels</title>
<link rel="stylesheet" href="https://fonts.googleapis.com/css2?family=Josefin+Sans:wght@400&family=Montserrat:wght@400;600&family=PT+Sans+Narrow:wght@400&display=swap">
<style>
  :root {
    --bg: #7d7d7d;
    --panel-top: #9fc8ec;
    --panel-mid: #d4e7f7;
    --panel-low: #a9cdee;
    --panel-edge: #8fbbe3;
    --ink: #141414;
    --ink-soft: #1e1e1e;
  }
  * { margin: 0; padding: 0; box-sizing: border-box; }
  html, body { width: 1200px; height: 1105px; overflow: hidden; }
  body {
    background: radial-gradient(ellipse at 50% 45%, #8f8f8f 0%, var(--bg) 70%, #6c6c6c 100%);
    position: relative;
    color: var(--ink);
  }
  .dieline {
    position: absolute;
    left: 290px; top: 122px;
    width: 620px; height: 860px;
    display: flex;
  }
  .panel {
    position: relative;
    width: 310px; height: 860px;
    overflow: hidden;
  }
  .panel-art {
    position: absolute; inset: 0;
    background:
      linear-gradient(115deg, rgba(255,255,255,0) 40%, rgba(255,255,255,0.18) 55%, rgba(255,255,255,0) 70%),
      linear-gradient(180deg, var(--panel-top) 0%, var(--panel-top) 22%, var(--panel-mid) 55%, var(--panel-low) 80%, var(--panel-edge) 100%);
  }
  .panel--side { border-left: 1px solid rgba(40,80,120,0.25); }

  .wordmark {
    position: absolute;
    writing-mode: vertical-rl;
    transform: rotate(180deg);
    font-family: "Josefin Sans", sans-serif;
    font-weight: 400;
    line-height: 1;
    letter-spacing: -2px;
    color: var(--ink);
  }
  .panel--front .wordmark { left: 40px; top: 60px; font-size: 200px; }
  .panel--side .wordmark { left: 36px; top: 24px; font-size: 140px; }

  .range-line {
    position: absolute;
    writing-mode: vertical-rl;
    transform: rotate(180deg);
    font-family: "Montserrat", sans-serif;
    font-size: 13px;
    letter-spacing: 0.5px;
    color: var(--ink-soft);
    left: 232px; top: 338px;
  }
  .claim {
    position: absolute;
    left: 0; right: 0; top: 628px;
    text-align: center;
    font-family: "Montserrat", sans-serif;
    font-weight: 600;
    font-size: 17px;
    line-height: 1.4;
    color: #1b1b1b;
  }
  .volume {
    position: absolute;
    left: 0; right: 0; top: 710px;
    text-align: center;
    font-family: "Montserrat", sans-serif;
    font-weight: 600;
    font-size: 15px;
    color: #1b1b1b;
  }
  .tagline {
    position: absolute;
    left: 0; right: 0; top: 800px;
    text-align: center;
    font-family: "Montserrat", sans-serif;
    font-weight: 400;
    font-size: 11px;
    letter-spacing: 2px;
    color: var(--ink-soft);
  }

  .description {
    position: absolute;
    left: 26px; top: 410px; width: 260px;
    font-family: "PT Sans Narrow", sans-serif;
    font-size: 14px;
    line-height: 1.22;
    color: #1f1f1f;
  }
  .instruction-title {
    position: absolute;
    left: 26px; top: 622px;
    font-family: "PT Sans Narrow", sans-serif;
    font-weight: 400;
    font-size: 21px;
    color: #1b1b1b;
  }
  .instruction {
    position: absolute;
    left: 26px;
    display: flex; align-items: center; gap: 10px;
    font-family: "PT Sans Narrow", sans-serif;
    font-size: 15px;
    color: #1b1b1b;
  }
  .instruction--weather { top: 672px; }
  .instruction--eyes { top: 728px; }
  .instruction svg { width: 30px; height: 30px; }
</style>
</head>
<body>
  <main class="dieline">
    <section class="panel panel--front">
      <div class="panel-art" role="img" aria-label="Soft blue background with faint diagonal light pattern"></div>
      <div class="wordmark">lumer</div>
      <div class="range-line">JAPANESE | SAKURA MASK</div>
      <p class="claim">NON-SURGERY<br>FACELIFT THERAPY</p>
      <p class="volume">300 ML</p>
      <p class="tagline">PROFESSIONAL SKINCARE THERAPIES</p>
    </section>

    <section class="panel panel--side">
      <div class="panel-art" role="img" aria-label="Soft blue background with faint diagonal light pattern"></div>
      <div class="wordmark">lumer</div>
      <p class="description">Lorem ipsum dolor sit amet, consectetur adipisicing elit, sed do eiusmod tempor incididunt ut labore et dolore magna aliqua. Ut enim ad minim veniam, quis nostrud exercitation ullamco laboris nisi ut aliquip ex ea commodo consequat. Duis aute irure dolor in reprehenderit in voluptate velit esse cillum dolore eu fugiat nulla pariatur. Excepteur sint occaecat cupidatat non proident, sunt in culpa qui officia deserunt mollit anim id est.</p>
      <h2 class="instruction-title">Instruction</h2>
      <div class="instruction instruction--weather">
        <svg viewBox="0 0 30 30" aria-hidden="true">
          <g fill="#141414">
            <circle cx="17" cy="11" r="5"/>
            <rect x="16" y="1" width="2" height="4"/>
            <rect x="16" y="17" width="2" height="3"/>
            <rect x="25" y="10" width="4" height="2"/>
            <rect x="6" y="10" width="4" height="2"/>
            <path d="M5 27a5 5 0 0 1 1-9.8A6 6 0 0 1 17 19a4 4 0 0 1 0 8z"/>
          </g>
        </svg>
        <span>Cloudy Weather</span>
      </div>
      <div class="instruction instruction--eyes">
        <svg viewBox="0 0 30 30" aria-hidden="true">
          <path fill="#141414" d="M8 28c-3-2-4-6-4-10v-6a2 2 0 0 1 4 0v5h1V5a2 2 0 0 1 4 0v11h1V3a2 2 0 0 1 4 0v13h1V5a2 2 0 0 1 4 0v12h1v-7a2 2 0 0 1 4 0v9c0 5-3 9-8 9z"/>
        </svg>
        <span>Don't Contact with eyes</span>
      </div>
    </section>
  </main>
</body>
</html>
```